Veltaro Clear Springs needs a new business card design (we produce and sell pure bottled water)

We need a clean modern design for our new business cards, We have an existing logo which ultimately cannot be changed, however it could be slighty improved and the colours adjusted. We have this existing logo on all of our bottles, vehicles etc.

Our company slogan is "Pure down to the last drop".
Along with our relevant company information
(Address, phone, website email etc) we will only be using names and not putting position titles for flexibilty.

We are looking for a clean, minimalist modern design.

You can view our website (if need of an update also!) to see our business.

Contact Information for Business Card

Staff Name : XXXXXX XXXXXX
Address : 8/41 Dunmore St
Halden Flats QLD 4261
Staff Mobile Number : 04XX XXX XXX
Office Phone Number : 07 3915 2047
Staff Email Address : XXXX@veltaroclearsprings.com.au
Website : www.veltaroclearsprings.com.au

Font styles to use
Sans Serif

Colors
cee9f5
33a6d7
0492cd
0455a3
3276b5
85abd2
cedeed

Requirements
Must have
• The ability to edit and change the staff members details as we will need to edit for each respective staff member (7 in total)

```html
<!DOCTYPE html>
<html lang="en">
<head>
<meta charset="utf-8">
<title>Veltaro Clear Springs – Business Card</title>
<link href="https://fonts.googleapis.com/css2?family=Arimo:wght@400;700&display=swap" rel="stylesheet">
<style>
  :root {
    --brand: #0455a3;
    --brand-mid: #3276b5;
    --brand-bright: #0492cd;
    --brand-soft: #cedeed;
    --ink: #111111;
    --paper: #ffffff;
    --text: #2a2a2a;
    --stage: #e4e6ea;
  }
  * { margin: 0; padding: 0; box-sizing: border-box; }
  html, body { width: 1200px; height: 997px; overflow: hidden; }
  body {
    background: var(--stage);
    font-family: "Arimo", Arial, sans-serif;
    display: flex; flex-direction: column; align-items: center; justify-content: center;
    gap: 60px;
  }
  .card {
    width: 560px; height: 320px; border-radius: 16px; position: relative; overflow: hidden;
    box-shadow: 0 6px 18px rgba(0,0,0,.18);
  }
  .card-front {
    background: var(--brand);
    display: flex; flex-direction: column; align-items: center; justify-content: center; gap: 18px;
  }
  .front-brand { display: flex; align-items: center; gap: 16px; color: var(--paper); }
  .brand-dot { width: 34px; height: 34px; border-radius: 50%; background: var(--paper); flex: none; }
  .brand-name { font-weight: 700; font-size: 34px; letter-spacing: 1px; text-transform: uppercase; line-height: 1.05; }
  .slogan { color: var(--brand-soft); font-size: 15px; letter-spacing: 1px; }
  .card-back { background: var(--paper); }
  .back-brand {
    position: absolute; top: 36px; right: 34px; display: flex; align-items: center; gap: 10px;
    color: var(--brand);
  }
  .back-brand .brand-dot { width: 20px; height: 20px; background: var(--brand); }
  .back-brand .brand-name { font-size: 20px; text-align: right; }
  .divider { position: absolute; left: 30px; right: 30px; top: 128px; height: 2px; background: var(--brand); }
  .staff-name {
    position: absolute; left: 30px; top: 142px; font-weight: 700; font-size: 19px; color: var(--brand);
    text-transform: uppercase; letter-spacing: .5px;
  }
  .contact-list { position: absolute; left: 30px; top: 182px; list-style: none; }
  .contact-list li { display: flex; align-items: center; gap: 9px; font-size: 14px; color: var(--text); height: 22px; }
  .contact-icon { width: 15px; height: 15px; flex: none; }
  .company-info {
    position: absolute; right: 34px; top: 142px; text-align: right; color: var(--ink);
    font-size: 13px; line-height: 1.35; font-style: normal;
  }
  .company-info .company-name { color: var(--brand); font-weight: 700; font-size: 15px; text-transform: uppercase; margin-bottom: 2px; }
  .footer-band { position: absolute; left: 0; bottom: 0; width: 560px; height: 70px; }
  .website {
    position: absolute; right: 30px; top: 274px; color: var(--paper); font-weight: 700; font-size: 14px;
    white-space: nowrap;
  }
</style>
</head>
<body>

<section class="card card-front" aria-label="Card front">
  <div class="front-brand">
    <span class="brand-dot"></span>
    <span class="brand-name">Veltaro<br>Clear Springs</span>
  </div>
  <p class="slogan">Pure down to the last drop</p>
</section>

<section class="card card-back" aria-label="Card back">
  <div class="back-brand">
    <span class="brand-dot"></span>
    <span class="brand-name">Veltaro<br>Clear Springs</span>
  </div>

  <div class="divider"></div>

  <h1 class="staff-name">Marlen Ostrova</h1>

  <ul class="contact-list">
    <li>
      <svg class="contact-icon" viewBox="0 0 16 16"><circle cx="8" cy="8" r="8" fill="#0455a3"/><path d="M5 4.5h2l.6 2-1 .8a5 5 0 0 0 2.1 2.1l.8-1 2 .6v2c-4 .3-6.8-2.5-6.5-6.5z" fill="#fff"/></svg>
      07 3915 2047
    </li>
    <li>
      <svg class="contact-icon" viewBox="0 0 16 16"><circle cx="8" cy="8" r="8" fill="#0455a3"/><rect x="5.5" y="3.8" width="5" height="8.4" rx="1" fill="#fff"/><rect x="6.4" y="5" width="3.2" height="5" fill="#0455a3"/></svg>
      04XX XXX XXX
    </li>
    <li>
      <svg class="contact-icon" viewBox="0 0 16 16"><circle cx="8" cy="8" r="8" fill="#0455a3"/><rect x="4" y="5.2" width="8" height="5.6" fill="#fff"/><path d="M4 5.2l4 3 4-3" fill="none" stroke="#0455a3" stroke-width="1"/></svg>
      XXXX@veltaroclearsprings.com.au
    </li>
  </ul>

  <address class="company-info">
    <div class="company-name">Veltaro Clear Springs</div>
    8/41 Dunmore St<br>
    Halden Flats QLD 4261
  </address>

  <svg class="footer-band" viewBox="0 0 560 70" preserveAspectRatio="none" aria-hidden="true">
    <polygon points="0,34 262,34 280,8 290,8 270,40 0,40" fill="#111111"/>
    <polygon points="0,46 274,46 292,18 560,18 560,70 0,70" fill="#0455a3"/>
  </svg>
  <div class="website">www.veltaroclearsprings.com.au</div>
</section>

</body>
</html>
```